Stationary Set Rebrand for Brenvik

We are a Canadian Distribution and Service Company that was established in 1969. Over the past 5 decades we have expanded our business and have warehouses across Canada. We specialize in adhesive tapes, adhesives, films, safety, warehouse, shipping, janitorial and packaging supplies.

We have updated our logo design and would like a new corporate branding identity that includes a new fresh Stationary Set (Business Cards, Letterhead, Letterhead MS Word, Envelope, Presentation Folders, Email Signatures, Notepad Covers, etc.)

Target Market(s)

Industrial Business Sector

Font styles to use
Sans Serif

Colors
0054AA
0677BA
7BADD7
CADEEF
E8F1F8
0094D4
00A9DD
6FCCEA
C7EBF8
E9F6FB
00AB8E
00BBA5
67D7C9
C6EFE9
E9F9F6
EB3D1F
EC4F4E
F09395
F8D3D4
FCEDEE

Requirements
Should not have
• Colors not too light, darker colours preferred

```html
<!DOCTYPE html>
<html lang="en">
<head>
<meta charset="utf-8">
<title>Brenvik Stationery Set</title>
<link href="https://fonts.googleapis.com/css2?family=Open+Sans:wght@400;600;800&display=swap" rel="stylesheet">
<style>
  :root {
    --ink: #1e1e1e;
    --red: #d7191f;
    --paper: #ffffff;
    --stage: #c8c8c8;
    --grey-text: #555555;
    --rule: #9a9a9a;
    --line: #d9d9d9;
  }
  * { box-sizing: border-box; margin: 0; padding: 0; }
  html, body { width: 703px; height: 1200px; overflow: hidden; }
  body {
    position: relative;
    background: var(--stage);
    font-family: "Open Sans", Arial, sans-serif;
    color: var(--ink);
  }
  .piece {
    position: absolute;
    background: var(--paper);
    box-shadow: 1px 2px 4px rgba(0,0,0,.35);
    overflow: hidden;
  }

  /* brand band along the foot of each item */
  .brand-band {
    position: absolute; left: 0; right: 0; bottom: 0;
    height: var(--band, 5px);
    background: var(--ink);
  }
  .brand-band::before,
  .brand-band::after {
    content: ""; position: absolute; top: 0; bottom: 0; right: 0;
  }
  .brand-band::before { left: var(--split, 48%); background: var(--paper); clip-path: polygon(var(--slope, 6px) 0, 100% 0, 100% 100%, 0 100%); }
  .brand-band::after { left: calc(var(--split, 48%) + var(--gap, 3px)); background: var(--red); clip-path: polygon(var(--slope, 6px) 0, 100% 0, 100% 100%, 0 100%); }

  /* name block */
  .logo { position: absolute; line-height: 1; }
  .logo .wordmark {
    display: block;
    font-weight: 800;
    font-size: var(--s);
    letter-spacing: -0.02em;
    color: var(--ink);
  }
  .logo .tagline {
    display: flex; align-items: center; gap: calc(var(--s) * .1);
    font-size: calc(var(--s) * .27);
    font-weight: 600;
    color: var(--ink);
    margin-top: calc(var(--s) * .06);
  }
  .logo .tagline::after {
    content: ""; width: calc(var(--s) * .22); height: calc(var(--s) * .22);
    background: var(--red);
  }
  .logo.on-dark .wordmark, .logo.on-dark .tagline { color: var(--paper); }

  /* contact lines */
  .contact-list { list-style: none; }
  .contact-list li { display: flex; align-items: center; gap: .3em; white-space: nowrap; }
  .contact-list svg { width: .8em; height: .8em; flex: none; fill: var(--red); }

  /* business card front */
  .card-front { left: 54px; top: 32px; width: 246px; height: 141px; }
  .card-front .logo { right: 15px; top: 13px; --s: 26px; }
  .card-front .person { position: absolute; left: 15px; top: 67px; right: 15px; border-bottom: 1px solid var(--rule); padding-bottom: 2px; }
  .person-name { color: var(--red); font-weight: 600; font-size: 9px; letter-spacing: .01em; }
  .person-role { color: var(--grey-text); font-size: 7px; }
  .card-front .contact-list { position: absolute; left: 15px; top: 97px; font-size: 7px; color: var(--grey-text); line-height: 1.3; }
  .card-front .address { position: absolute; right: 15px; top: 106px; font-size: 7px; text-align: right; color: var(--grey-text); line-height: 1.3; }

  /* window envelope front */
  .envelope-front { left: 319px; top: 33px; width: 326px; height: 141px; }
  .envelope-front .logo { left: 9px; top: 9px; --s: 12px; }
  .envelope-front .address { position: absolute; left: 9px; top: 24px; font-size: 4px; color: var(--grey-text); line-height: 1.35; }

  /* business card back */
  .card-back { left: 54px; top: 197px; width: 246px; height: 141px; }
  .card-back .pattern { position: absolute; inset: 0; background: linear-gradient(90deg, #161616 0%, #1d1d1d 45%, #3a3a3a 100%); }
  .card-back .logo { left: 83px; top: 58px; --s: 18px; }

  /* envelope back */
  .envelope-back { left: 318px; top: 195px; width: 329px; height: 142px; }
  .envelope-back .flap { position: absolute; left: 0; top: 0; width: 100%; height: 45px; }
  .envelope-back .logo { left: 128px; top: 8px; --s: 17px; }

  /* letter sheet layout */
  .sheet-head { position: absolute; left: 14px; right: 10px; top: 12px; height: 25px; border-bottom: .6px solid var(--rule); }
  .sheet-head .logo { left: 0; top: 0; --s: 16px; }
  .sheet-head .contact-block { position: absolute; right: 0; top: 0; font-size: 2.6px; color: var(--grey-text); line-height: 1.35; }
  .letter { position: absolute; left: 18px; right: 19px; font-size: 2.3px; line-height: 1.4; color: #333; }
  .letter .salutation { font-weight: 600; font-size: 3.3px; margin-bottom: 7px; }
  .letter p { margin-bottom: 3.5px; text-align: justify; }
  .letter .closing { font-weight: 600; font-size: 2.3px; margin-top: 7px; }
  .signature { display: block; width: 34px; height: 8px; margin-top: 6px; background: linear-gradient(90deg, #bcbcbc, #e6e6e6); }

  .letterhead { left: 38px; top: 363px; width: 203px; height: 286px; }
  .letterhead .letter { top: 88px; }

  /* folder outside */
  .folder-cover { left: 264px; top: 363px; width: 401px; height: 284px; }
  .folder-cover .spine { position: absolute; left: 0; top: 0; bottom: 0; width: 200px; background: var(--ink); }
  .folder-cover .spine .logo { left: 27px; top: 121px; --s: 36px; }
  .folder-cover .inner-page { position: absolute; left: 200px; top: 0; bottom: 0; right: 0; background: linear-gradient(90deg, #e8e8e8, #ffffff 40%); }
  .folder-cover .inner-page .sheet-head { left: 13px; right: 10px; }
  .folder-cover .brand-band { --split: 74%; }

  /* notepad */
  .notepad { left: 38px; top: 663px; width: 203px; height: 285px; }
  .notepad .ruled { position: absolute; left: 17px; right: 17px; top: 46px; height: 210px;
    background: repeating-linear-gradient(to bottom, transparent 0 8.2px, var(--line) 8.2px 8.8px); }

  /* folder inside */
  .folder-open { left: 266px; top: 663px; width: 398px; height: 285px; background: transparent; box-shadow: none; }
  .folder-open .panel-left { position: absolute; left: 0; top: 0; width: 199px; height: 100%; background: linear-gradient(90deg, #ffffff 40%, #dedede); }
  .folder-open .panel-right { position: absolute; left: 199px; top: 0; right: 0; height: 100%; background: linear-gradient(90deg, #c9c9c9, #f2f2f2 40%, #ffffff); }
  .folder-open .inserted-page { position: absolute; left: 211px; top: 12px; width: 177px; height: 200px; background: linear-gradient(90deg, #ffffff 60%, #f0f0f0); }
  .folder-open .inserted-page .sheet-head { left: 12px; right: 8px; top: 10px; height: 22px; }
  .folder-open .inserted-page .sheet-head .logo { --s: 15px; }
  .folder-open .inserted-page .letter { top: 88px; left: 16px; right: 16px; }
  .folder-open .pockets { position: absolute; left: 0; top: 181px; width: 398px; height: 104px; }

  /* large business card */
  .card-large { left: 133px; top: 982px; width: 437px; height: 170px; }
  .card-large .logo { left: 22px; top: 20px; --s: 44px; }
  .card-large .person { position: absolute; right: 24px; top: 25px; text-align: right; }
  .card-large .person-name { font-size: 15.5px; font-weight: 400; letter-spacing: .02em; }
  .card-large .person-role { font-size: 12px; }
  .card-large .contact-list { position: absolute; left: 23px; top: 100px; font-size: 12.5px; color: var(--grey-text); line-height: 1.3; }
  .card-large .address { position: absolute; right: 24px; top: 116px; text-align: right; font-size: 12.5px; color: var(--grey-text); line-height: 1.3; }
  .card-large .brand-band { --band: 11px; --split: 48%; --slope: 11px; --gap: 4px; }
</style>
</head>
<body>

<svg width="0" height="0" style="position:absolute">
  <symbol id="icon-phone" viewBox="0 0 10 10"><path d="M1 3c0-1 1-2 4-2s4 1 4 2v1H7V3H3v1H1zM2 5h6l1 4H1z"/></symbol>
  <symbol id="icon-mail" viewBox="0 0 10 10"><path d="M1 2h8v6H1zM1.8 2.8v.4L5 5.5l3.2-2.3v-.4z" fill-rule="evenodd"/></symbol>
  <symbol id="icon-globe" viewBox="0 0 10 10"><circle cx="5" cy="5" r="4.3"/></symbol>
</svg>

<!-- Business card front -->
<section class="piece card-front">
  <div class="logo"><span class="wordmark">Brenvik</span><span class="tagline">Tape and Packaging Specialists</span></div>
  <div class="person">
    <div class="person-name">DANIEL HARPER</div>
    <div class="person-role">Managing Director</div>
  </div>
  <ul class="contact-list">
    <li><svg><use href="#icon-phone"/></svg>044-987 654 321</li>
    <li><svg><use href="#icon-mail"/></svg>info@brenvik.com</li>
    <li><svg><use href="#icon-globe"/></svg>www.brenvik.com</li>
  </ul>
  <div class="address">Your Address, City<br>State, Zip 0000</div>
  <div class="brand-band" style="--band:5px;--split:48%;--slope:6px;"></div>
</section>

<!-- Envelope front -->
<section class="piece envelope-front">
  <div class="logo"><span class="wordmark">Brenvik</span><span class="tagline">Tape and Packaging Specialists</span></div>
  <div class="address">Your Address, City<br>State, Zip 0000</div>
  <div class="brand-band" style="--band:5px;--split:82%;--slope:5px;"></div>
</section>

<!-- Business card back -->
<section class="piece card-back">
  <div class="pattern" role="img" aria-label="Repeating leaf pattern in dark greys"></div>
  <div class="logo on-dark"><span class="wordmark">Brenvik</span><span class="tagline">Tape and Packaging Specialists</span></div>
</section>

<!-- Envelope back -->
<section class="piece envelope-back">
  <svg class="flap" viewBox="0 0 329 45" preserveAspectRatio="none" aria-hidden="true">
    <path d="M0 0H329L320 30Q316 40 300 40H28Q14 40 10 30Z" fill="#ffffff" stroke="#d4d4d4" stroke-width="1"/>
  </svg>
  <div class="logo"><span class="wordmark">Brenvik</span><span class="tagline">Tape and Packaging Specialists</span></div>
</section>

<!-- Letterhead -->
<section class="piece letterhead">
  <header class="sheet-head">
    <div class="logo"><span class="wordmark">Brenvik</span><span class="tagline">Tape and Packaging Specialists</span></div>
    <ul class="contact-list contact-block">
      <li>Your Address, City</li>
      <li>State, Zip 0000</li>
      <li><svg><use href="#icon-phone"/></svg>044-987 654 321</li>
      <li><svg><use href="#icon-mail"/></svg>info@brenvik.com</li>
      <li><svg><use href="#icon-globe"/></svg>www.brenvik.com</li>
    </ul>
  </header>
  <article class="letter">
    <div class="salutation">Dear Mr. Harper,</div>
    <p>Thank you for choosing our team for your packaging needs. We are pleased to confirm that your order of tapes, films and shipping supplies has been scheduled for delivery this week.</p>
    <p>Our warehouses across the country stock a full range of adhesives, safety and janitorial products, so future orders can be filled quickly and shipped from the location nearest to you.</p>
    <p>Your account manager will contact you to review pricing and volumes for the coming quarter. Please let us know if you would like samples of our new stretch films before then.</p>
    <p>We appreciate your continued business and look forward to serving you for many years to come.</p>
    <div class="closing">Sincerely,</div>
    <span class="signature" role="img" aria-label="Handwritten signature"></span>
  </article>
  <div class="brand-band" style="--band:4px;--split:49%;--slope:4px;"></div>
</section>

<!-- Presentation folder, outside -->
<section class="piece folder-cover">
  <div class="spine">
    <div class="logo on-dark"><span class="wordmark">Brenvik</span><span class="tagline">Tape and Packaging Specialists</span></div>
  </div>
  <div class="inner-page">
    <header class="sheet-head">
      <div class="logo"><span class="wordmark">Brenvik</span><span class="tagline">Tape and Packaging Specialists</span></div>
      <ul class="contact-list contact-block">
        <li>Your Address, City</li>
        <li>State, Zip 0000</li>
        <li><svg><use href="#icon-phone"/></svg>044-987 654 321</li>
        <li><svg><use href="#icon-mail"/></svg>info@brenvik.com</li>
        <li><svg><use href="#icon-globe"/></svg>www.brenvik.com</li>
      </ul>
    </header>
  </div>
  <div class="brand-band" style="--band:4px;--slope:4px;"></div>
</section>

<!-- Notepad -->
<section class="piece notepad">
  <header class="sheet-head">
    <div class="logo"><span class="wordmark">Brenvik</span><span class="tagline">Tape and Packaging Specialists</span></div>
    <ul class="contact-list contact-block">
      <li>Your Address, City</li>
      <li>State, Zip 0000</li>
      <li><svg><use href="#icon-phone"/></svg>044-987 654 321</li>
      <li><svg><use href="#icon-mail"/></svg>info@brenvik.com</li>
      <li><svg><use href="#icon-globe"/></svg>www.brenvik.com</li>
    </ul>
  </header>
  <div class="ruled"></div>
  <div class="brand-band" style="--band:4px;--split:49%;--slope:4px;"></div>
</section>

<!-- Presentation folder, inside -->
<section class="piece folder-open">
  <div class="panel-left"></div>
  <div class="panel-right"></div>
  <div class="inserted-page">
    <header class="sheet-head">
      <div class="logo"><span class="wordmark">Brenvik</span><span class="tagline">Tape and Packaging Specialists</span></div>
      <ul class="contact-list contact-block">
        <li>Your Address, City</li>
        <li>State, Zip 0000</li>
        <li><svg><use href="#icon-phone"/></svg>044-987 654 321</li>
        <li><svg><use href="#icon-mail"/></svg>info@brenvik.com</li>
        <li><svg><use href="#icon-globe"/></svg>www.brenvik.com</li>
      </ul>
    </header>
    <article class="letter" style="top:63px;">
      <div class="salutation">Dear Mr. Harper,</div>
      <p>Thank you for choosing our team for your packaging needs. We are pleased to confirm that your order of tapes, films and shipping supplies has been scheduled for delivery this week.</p>
      <p>Our warehouses across the country stock a full range of adhesives, safety and janitorial products, so future orders can be filled quickly and shipped from the location nearest to you.</p>
      <p>Your account manager will contact you to review pricing and volumes for the coming quarter. Please let us know if you would like samples of our new stretch films before then.</p>
      <p>We appreciate your continued business and look forward to serving you for many years to come.</p>
      <div class="closing">Sincerely,</div>
    </article>
  </div>
  <svg class="pockets" viewBox="0 0 398 104" preserveAspectRatio="none" aria-hidden="true">
    <path d="M0 0H180Q188 0 190 10L199 93L199 104H0Z" fill="#1e1e1e"/>
    <path d="M398 0H218Q210 0 208 10L199 93L199 104H398Z" fill="#1e1e1e"/>
  </svg>
</section>

<!-- Large business card -->
<section class="piece card-large">
  <div class="logo"><span class="wordmark">Brenvik</span><span class="tagline">Tape and Packaging Specialists</span></div>
  <div class="person">
    <div class="person-name">DANIEL HARPER</div>
    <div class="person-role">Managing Director</div>
  </div>
  <ul class="contact-list">
    <li><svg><use href="#icon-phone"/></svg>044-987 654 321</li>
    <li><svg><use href="#icon-mail"/></svg>info@brenvik.com</li>
    <li><svg><use href="#icon-globe"/></svg>www.brenvik.com</li>
  </ul>
  <div class="address">Your Address<br>City, State, Zip 0000</div>
  <div class="brand-band"></div>
</section>

</body>
</html>
```